Steps to get a free fence estimate

Hi! I need a new flyer in the similar design / style that you created previously for us! I would like this one to showcase the steps to get a free estimate.
There are several options to obtain a free fence quote for your fence installation or to buy fence materials:
1) In-Person - In-person quotes are available for fence installations only. Call, email or message us online to schedule an in-person measurement at your property.
2) Virtual Quotes - Send us your lot survey, fence layout diagram with dimensions, or measure your property online using our Web Yard Sizing Helper. We can review the dimensions to provide a site-unseen quote. You can also call us with your project information for a quote via phone.
3) Competitor Quotes - Send us the quotes from qualified competitors for price comparisons. Competitor quotes must have fence style, footage, and other project information.
What information do we need to give you a free estimate?
Fence footage - how many feet of fencing do you need?
Fence style - what fence style and material would you like quoted?
Fence placement - does the fence need to be installed in concrete or asphalt surfaces? or will it be installed in normal dirt areas?
Gate information - do you need any single person walk through gates, or a larger double gate? (walk gates can be 3FT, 4FT and 5FT wide - 5FT wide is wide enough for a riding lawn mower to get through. double gates can be 8FT, 10FT and 12FT wide.)
For installation quotes, please let us know any additional information such as if there is any existing fencing to remove, obstacles in the path of the fence line or if the fence has to be installed on top of concrete/asphalt surfaces.
We make the fence quoting process easy and simple!
Lifetime warranty on workmanship, labor and manufacturer's lifetime warranty on materials.
---
This flyer only needs to discuss the steps to obtaining a free fence estimate for our customers.

```html
<!DOCTYPE html>
<html lang="en">
<head>
<meta charset="utf-8">
<title>Steps to a New Fence Installation</title>
<link rel="stylesheet" href="https://fonts.googleapis.com/css2?family=Roboto:wght@400;700;900&family=Montserrat:wght@400;700&display=swap">
<style>
  :root {
    --paper: #f7f7f6;
    --ink: #111418;
    --navy: #0d3357;
    --grey: #555a60;
    --violet: #3f2a6b;
    --orange: #f47b20;
    --yellow: #fcd704;
    --magenta: #d9318f;
    --teal: #16a9b3;
    --teal-deep: #05a88c;
    --line: #3f2a6b;
  }
  * { margin: 0; padding: 0; box-sizing: border-box; }
  html, body { width: 1200px; height: 1114px; overflow: hidden; background: var(--paper); }
  .flyer { position: relative; width: 1200px; height: 1114px; font-family: "Roboto", sans-serif; color: var(--ink); }

  .header {
    position: absolute; left: 0; top: 0; width: 1200px; height: 110px;
    background: linear-gradient(90deg, var(--orange) 0%, #f68e25 45%, var(--yellow) 100%);
    display: flex; align-items: center; justify-content: center;
  }
  .header h1 { color: #fff; font-weight: 900; font-size: 54px; letter-spacing: -0.5px; }

  .info-title {
    position: absolute; left: 67px; top: 148px;
    font-weight: 700; font-size: 34px; line-height: 42px; text-transform: uppercase;
  }
  .info-row { position: absolute; left: 67px; width: 520px; }
  .info-label { position: absolute; left: 0; top: 0; width: 125px; font-weight: 700; font-size: 19px; line-height: 18px; }
  .info-text { position: absolute; left: 135px; top: 0; width: 390px; font-size: 16.5px; line-height: 23px; color: var(--grey); }
  .label-orange { color: var(--orange); }
  .label-teal { color: var(--teal); }
  .label-navy { color: var(--navy); }
  .label-pink { color: var(--magenta); }

  .timeline { position: absolute; left: 0; top: 0; width: 1200px; height: 760px; }

  .step { position: absolute; left: 835px; width: 310px; font-family: "Montserrat", sans-serif; }
  .step h2 { font-size: 19px; font-weight: 700; color: var(--violet); letter-spacing: 0.3px; margin-bottom: 8px; }
  .step p { font-size: 13.4px; line-height: 17px; color: var(--grey); }

  .teal-band {
    position: absolute; left: 46px; top: 826px; width: 1107px; height: 137px;
    background: linear-gradient(90deg, var(--teal) 0%, var(--teal-deep) 100%);
    border-radius: 0 0 42px 42px;
  }
  .band-gap {
    position: absolute; left: 73px; top: 760px; width: 1053px; height: 142px;
    background: var(--paper); border-radius: 0 0 44px 44px;
  }
  .note {
    position: absolute; left: 84px; top: 769px; width: 1032px; height: 124px;
    border-radius: 44px;
    background: linear-gradient(90deg, var(--magenta) 0%, #e8506d 55%, var(--orange) 100%);
    color: #fff; font-weight: 700; font-size: 23.5px; line-height: 29px; text-align: center;
    display: flex; align-items: center; justify-content: center; padding: 0 18px;
  }
  .band-text {
    position: absolute; left: 46px; top: 914px; width: 1107px; text-align: center;
    color: #fff; font-weight: 700; font-size: 24.5px; letter-spacing: 0.2px;
  }
  .warranty {
    position: absolute; left: 0; top: 974px; width: 1200px; text-align: center;
    color: var(--navy); font-weight: 700; font-size: 31px; line-height: 38px;
  }
  .rule { position: absolute; top: 1036px; height: 2px; background: var(--navy); }
  .rule-left { left: 0; width: 374px; }
  .rule-right { left: 820px; width: 380px; }
</style>
</head>
<body>
<main class="flyer">
  <header class="header"><h1>Steps to a New Fence Installation</h1></header>

  <h2 class="info-title">What information<br>do we need to give you<br>a free estimate?</h2>

  <div class="info-row" style="top:314px">
    <div class="info-label label-orange">Fence<br>footage -</div>
    <div class="info-text" style="top:7px">how many feet of fencing do you need?</div>
  </div>
  <div class="info-row" style="top:406px">
    <div class="info-label label-teal">Fence style -</div>
    <div class="info-text" style="top:-10px">what fence style and material would you like quoted?</div>
  </div>
  <div class="info-row" style="top:482px">
    <div class="info-label label-navy">Fence<br>placement -</div>
    <div class="info-text" style="top:-3px">Does the fence need to be installed in concrete or asphalt surfaces? or will it be installed in normal dirt areas?</div>
  </div>
  <div class="info-row" style="top:584px">
    <div class="info-label label-pink">Gate<br>information -</div>
    <div class="info-text" style="left:137px;width:400px;top:-6px">Do you need any single person walk through gates, or a larger double gate? (walk gates can be 3FT, 4FT and 5FT wide - 5FT wide is wide enough for a riding lawn mower to get through. double gates can be 8FT, 10FT and 12FT wide.)</div>
  </div>

  <svg class="timeline" viewBox="0 0 1200 760" aria-hidden="true">
    <defs>
      <linearGradient id="pin-one" x1="0" x2="1" y1="0" y2="1">
        <stop offset="0" stop-color="#d9318f"/><stop offset="1" stop-color="#f1602f"/>
      </linearGradient>
      <linearGradient id="pin-two" x1="0" x2="1" y1="1" y2="0">
        <stop offset="0" stop-color="#f26a22"/><stop offset="1" stop-color="#fcd704"/>
      </linearGradient>
      <linearGradient id="pin-three" x1="0" x2="1" y1="0" y2="1">
        <stop offset="0" stop-color="#13b3c4"/><stop offset="1" stop-color="#068a78"/>
      </linearGradient>
      <filter id="soft" x="-30%" y="-30%" width="160%" height="160%">
        <feDropShadow dx="0" dy="2" stdDeviation="3" flood-opacity="0.3"/>
      </filter>
    </defs>
    <line x1="608" y1="152" x2="608" y2="742" stroke="var(--line)" stroke-width="1.5"/>
    <path d="M608 142 l-6 12 h12 z" fill="var(--line)"/>
    <path d="M608 752 l-6 -12 h12 z" fill="var(--line)"/>

    <g transform="translate(751 260)">
      <line x1="-143" y1="0" x2="-74" y2="0" stroke="var(--line)" stroke-width="1.5"/>
      <circle cx="-143" cy="0" r="11" fill="#fff" stroke="var(--line)" stroke-width="1.5"/>
      <circle cx="-143" cy="0" r="5.5" fill="#d9318f"/>
      <path d="M-74 0 C-56 0 -46 -44 0 -52 A52 52 0 1 1 0 52 C-46 44 -56 0 -74 0 Z" fill="url(#pin-one)"/>
      <circle r="39" fill="#fff" filter="url(#soft)"/>
      <text y="19" text-anchor="middle" font-family="Montserrat, sans-serif" font-weight="700" font-size="52" fill="#0d3357">1</text>
    </g>
    <g transform="translate(751 445)">
      <line x1="-143" y1="0" x2="-74" y2="0" stroke="var(--line)" stroke-width="1.5"/>
      <circle cx="-143" cy="0" r="11" fill="#fff" stroke="var(--line)" stroke-width="1.5"/>
      <circle cx="-143" cy="0" r="5.5" fill="#f47b20"/>
      <path d="M-74 0 C-56 0 -46 -44 0 -52 A52 52 0 1 1 0 52 C-46 44 -56 0 -74 0 Z" fill="url(#pin-two)"/>
      <circle r="39" fill="#fff" filter="url(#soft)"/>
      <text y="19" text-anchor="middle" font-family="Montserrat, sans-serif" font-weight="700" font-size="52" fill="#0d3357">2</text>
    </g>
    <g transform="translate(751 629)">
      <line x1="-143" y1="0" x2="-74" y2="0" stroke="var(--line)" stroke-width="1.5"/>
      <circle cx="-143" cy="0" r="11" fill="#fff" stroke="var(--line)" stroke-width="1.5"/>
      <circle cx="-143" cy="0" r="5.5" fill="#0aa88a"/>
      <path d="M-74 0 C-56 0 -46 -44 0 -52 A52 52 0 1 1 0 52 C-46 44 -56 0 -74 0 Z" fill="url(#pin-three)"/>
      <circle r="39" fill="#fff" filter="url(#soft)"/>
      <text y="19" text-anchor="middle" font-family="Montserrat, sans-serif" font-weight="700" font-size="52" fill="#0d3357">3</text>
    </g>
  </svg>

  <section class="step" style="top:196px">
    <h2>IN-PERSON</h2>
    <p>In-person quotes are available for fence installations only. Call, email or message us online to schedule an in-person measurement at your property.</p>
  </section>
  <section class="step" style="top:365px">
    <h2>VIRTUAL QUOTES</h2>
    <p>Send us your lot survey, fence layout diagram with dimensions, or measure your property online using our Web Yard Sizing Helper. We can review the dimensions to provide a site-unseen quote. You can also call us with your project information for a quote via phone.</p>
  </section>
  <section class="step" style="top:580px">
    <h2>COMPETITOR QUOTES</h2>
    <p>Send us the quotes from qualified competitors for price comparisons. Competitor quotes must have fence style, footage, and other project information.</p>
  </section>

  <div class="teal-band"></div>
  <div class="band-gap"></div>
  <div class="note">For installation quotes, please let us know any additional information such as if there is any existing fencing to remove, obstacles in the path of the fence line or if the fence has to be installed on top of concrete/asphalt surfaces.</div>
  <div class="band-text">WE MAKE THE FENCE QUOTING PROCESS EASY AND SIMPLE!</div>

  <div class="rule rule-left"></div>
  <div class="rule rule-right"></div>
  <p class="warranty">Lifetime warranty on workmanship, labor and manufacturer's<br>lifetime warranty on materials.</p>
</main>
</body>
</html>
```